Logo + Business Card design for a new start-up

For a new start-up company, a global brand expansion agency (marketing, brand consulting solutions) we're looking for a creative designer to help us design both the company logo and business card for project managers.

The name of the company is 'Harrow Mark Partners' (abbreviated: HMP, website: harrowmarkpartners.example)

The logo design should give the company an image of "corporate" (serious), but not too plain/simple. Playing with overlapping fonts, or font colors is an option. Logo with only the abbreviation HMP is also an option.

The business cards need to have a touch of creativity to them, any style/colors can be used, and should underline the nature of business.

Industry/Entity Type

Business

```html
<!DOCTYPE html>
<html lang="en">
<head>
<meta charset="utf-8">
<title>Harrow Mark Partners – Business Card</title>
<link rel="stylesheet" href="https://fonts.googleapis.com/css2?family=Questrial&family=Open+Sans:wght@800&display=swap">
<style>
  :root {
    --brand-red: #dc3c26;
    --card-light: #f2f2f2;
    --page: #ffffff;
    --ink: #1e1e1e;
    --white: #ffffff;
  }
  html, body {
    margin: 0;
    padding: 0;
    width: 985px;
    height: 1200px;
    overflow: hidden;
    background: var(--page);
  }
  .canvas {
    position: relative;
    width: 985px;
    height: 1200px;
    font-family: "Questrial", "Century Gothic", sans-serif;
  }
  .card {
    position: absolute;
    left: 94px;
    width: 800px;
    height: 481px;
  }
  .card--front {
    top: 109px;
    background: var(--brand-red);
  }
  .card--back {
    top: 631px;
    left: 99px;
    width: 798px;
    height: 480px;
    background: var(--card-light);
  }
  .wordmark {
    position: absolute;
    margin: 0;
    font-family: "Questrial", "Century Gothic", sans-serif;
    font-weight: 400;
    line-height: 1.05;
    letter-spacing: 1px;
  }
  .card--front .wordmark {
    left: 0;
    right: 0;
    top: 198px;
    text-align: center;
    font-size: 34px;
    color: var(--white);
  }
  .card--back .wordmark {
    left: 115px;
    top: 200px;
    font-size: 29px;
    color: var(--ink);
  }
  .front-url {
    position: absolute;
    left: 0;
    right: 0;
    top: 436px;
    text-align: center;
    font-size: 20px;
    color: var(--white);
    letter-spacing: 0.3px;
  }
  .divider-dots {
    position: absolute;
    left: 364px;
    top: 147px;
  }
  .contact {
    position: absolute;
    left: 398px;
    top: 149px;
    color: var(--brand-red);
  }
  .contact__name {
    margin: 0;
    font-family: "Open Sans", "Arial", sans-serif;
    font-weight: 800;
    font-size: 36px;
    line-height: 1;
    letter-spacing: 3px;
  }
  .contact__role {
    margin: 2px 0 0;
    width: 221px;
    text-align: right;
    font-size: 16px;
    line-height: 1;
  }
  .contact__line {
    margin: 0;
    font-size: 20px;
    line-height: 1.3;
  }
  .contact__phone { margin-top: 30px; }
  .contact__web {
    margin-top: 14px;
    line-height: 0.78;
  }
</style>
</head>
<body>
<main class="canvas">
  <section class="card card--front" aria-label="Card front">
    <p class="wordmark">HARROW MARK<br>PARTNERS</p>
    <p class="front-url">www.harrowmarkpartners.example</p>
  </section>

  <section class="card card--back" aria-label="Card back">
    <p class="wordmark">HARROW MARK<br>PARTNERS</p>

    <svg class="divider-dots" width="10" height="222" viewBox="0 0 10 222" aria-hidden="true">
      <g fill="#dc3c26">
        <circle cx="5" cy="4" r="3"/><circle cx="5" cy="12" r="3"/><circle cx="5" cy="20" r="3"/>
        <circle cx="5" cy="28" r="3"/><circle cx="5" cy="36" r="3"/><circle cx="5" cy="44" r="3"/>
        <circle cx="5" cy="52" r="3"/><circle cx="5" cy="60" r="3"/><circle cx="5" cy="68" r="3"/>
        <circle cx="5" cy="76" r="3"/><circle cx="5" cy="84" r="3"/><circle cx="5" cy="92" r="3"/>
        <circle cx="5" cy="100" r="3"/><circle cx="5" cy="108" r="3"/><circle cx="5" cy="116" r="3"/>
        <circle cx="5" cy="124" r="3"/><circle cx="5" cy="132" r="3"/><circle cx="5" cy="140" r="3"/>
        <circle cx="5" cy="148" r="3"/><circle cx="5" cy="156" r="3"/><circle cx="5" cy="164" r="3"/>
        <circle cx="5" cy="172" r="3"/><circle cx="5" cy="180" r="3"/><circle cx="5" cy="188" r="3"/>
        <circle cx="5" cy="196" r="3"/><circle cx="5" cy="204" r="3"/><circle cx="5" cy="212" r="3"/>
        <circle cx="5" cy="220" r="2"/>
      </g>
    </svg>

    <div class="contact">
      <h1 class="contact__name">MARA QUILL</h1>
      <p class="contact__role">POSITION</p>
      <p class="contact__line contact__phone">+944 8305716204</p>
      <p class="contact__line">maraquill@hmpmail.example</p>
      <p class="contact__line contact__web">www.harrowmarkpartners.example<br>www.harrowmarkpartners.example</p>
    </div>
  </section>
</main>
</body>
</html>
```